Roaming outings business card

please see website
www.roamingoutings.comau

info needed on card
Keiran Voss
Ph
email
Adventure Riding GPS trails

please use my logo and colours off my site

Business

Keiran Voss
keiran@roamingoutings.com

```html
<!DOCTYPE html>
<html lang="en">
<head>
<meta charset="utf-8">
<title>Roaming Outings – Business Card</title>
<link href="https://fonts.googleapis.com/css2?family=Arimo:wght@400;700&display=swap" rel="stylesheet">
<style>
  :root {
    --stage: #e9e6e1;
    --card-white: #ffffff;
    --card-black: #111111;
    --accent-yellow: #f5d21f;
    --mark-grey: #6b6b6b;
    --text-light: #ffffff;
    --text-dark: #1a1a1a;
  }
  * { margin: 0; padding: 0; box-sizing: border-box; }
  html, body {
    width: 1200px;
    height: 892px;
    overflow: hidden;
    background: var(--stage);
    font-family: "Arimo", Arial, sans-serif;
  }
  .canvas {
    position: relative;
    width: 1200px;
    height: 892px;
  }
  .card {
    position: absolute;
    width: 540px;
    height: 309px;
    border-radius: 4px;
    overflow: hidden;
    box-shadow: 0 10px 26px rgba(0,0,0,0.22);
  }

  /* Back of card */
  .card--back {
    left: 600px;
    top: 120px;
    background: var(--card-black);
    display: flex;
    align-items: center;
    justify-content: center;
    gap: 26px;
  }
  .brand {
    display: flex;
    align-items: center;
    gap: 26px;
  }
  .brand__dot {
    width: 84px;
    height: 84px;
    border-radius: 50%;
    background: var(--accent-yellow);
    flex: none;
  }
  .brand__name {
    font-weight: 700;
    text-transform: uppercase;
    line-height: 0.95;
    letter-spacing: 0.5px;
  }
  .card--back .brand__name { color: var(--text-light); font-size: 44px; }

  /* Front of card */
  .card--front {
    left: 60px;
    top: 470px;
    background: var(--card-white);
  }
  .card__head {
    height: 160px;
    display: flex;
    align-items: center;
    justify-content: center;
  }
  .card--front .brand__name { color: var(--text-dark); font-size: 40px; }
  .card--front .brand__dot { width: 72px; height: 72px; }
  .card__stripe {
    height: 7px;
    background: var(--accent-yellow);
  }
  .card__band {
    height: 142px;
    background: var(--card-black);
    display: flex;
    align-items: center;
    padding: 0 24px 0 34px;
    color: var(--text-light);
  }
  .person {
    font-size: 31px;
    font-weight: 400;
    white-space: nowrap;
    padding-right: 16px;
  }
  .divider {
    width: 1px;
    height: 64px;
    background: var(--text-light);
    margin-right: 14px;
  }
  .contacts {
    list-style: none;
    display: flex;
    flex-direction: column;
    gap: 8px;
    font-size: 16px;
  }
  .contacts li {
    display: flex;
    align-items: center;
    gap: 10px;
    white-space: nowrap;
  }
  .contacts svg { width: 16px; height: 16px; flex: none; }
</style>
</head>
<body>
<main class="canvas">

  <section class="card card--back" aria-label="Business card back">
    <div class="brand">
      <span class="brand__dot"></span>
      <span class="brand__name">Roaming<br>Outings</span>
    </div>
  </section>

  <section class="card card--front" aria-label="Business card front">
    <header class="card__head">
      <div class="brand">
        <span class="brand__dot"></span>
        <span class="brand__name">Roaming<br>Outings</span>
      </div>
    </header>
    <div class="card__stripe"></div>
    <div class="card__band">
      <p class="person">Keiran Voss</p>
      <span class="divider"></span>
      <ul class="contacts">
        <li>
          <svg viewBox="0 0 16 16" aria-hidden="true">
            <rect x="0.5" y="0.5" width="15" height="15" rx="2" fill="#fff"/>
            <path d="M4 5c0-1 1-1.5 2-1.5h4c1 0 2 .5 2 1.5v1H10V5H6v1H4z" fill="#111"/>
            <rect x="4" y="7" width="8" height="5" rx="1" fill="#111"/>
          </svg>
          <span>keiran@roamingoutings.com</span>
        </li>
        <li>
          <svg viewBox="0 0 16 16" aria-hidden="true">
            <rect x="0.5" y="0.5" width="15" height="15" rx="2" fill="#fff"/>
            <circle cx="8" cy="8" r="5" fill="none" stroke="#111" stroke-width="1.4"/>
            <path d="M3 8h10M8 3c-2 2.5-2 7.5 0 10M8 3c2 2.5 2 7.5 0 10" fill="none" stroke="#111" stroke-width="1"/>
          </svg>
          <span>www.roamingoutings.com.au</span>
        </li>
      </ul>
    </div>
  </section>

</main>
</body>
</html>
```